Harborline Crest Insurance Services

we are a high end insurance agency we specialize on Auto | Home | Business | Life looking for something professional and luxuries at the same time. if you guys need anything else please let me know.

Auto | Home | Business | Life must be under logo on the back with black background.

i want the back part to be black with our gold logo on it.

Target Market(s)

Auto | Home | Business | Life

Industry/Entity Type

Insurance Broker

Contact Information for Business Card

My logo is gold so a black in the back would be nice.

Font styles to use
Serif

Colors
000000

Requirements
Must have
• Big logo on the back with black background.

```html
<!DOCTYPE html>
<html lang="en">
<head>
<meta charset="utf-8">
<title>Harborline Crest Insurance Services — Business Card</title>
<link href="https://fonts.googleapis.com/css2?family=Cinzel:wght@600&family=Tinos&family=Montserrat:wght@300;500&display=swap" rel="stylesheet">
<style>
  :root {
    --stage: #2a2422;
    --card: #0b0b0b;
    --gold: #f2c21b;
    --silver: #c9c9c9;
    --silver-dim: #8e8e8e;
    --white: #e8e8e8;
  }
  * { box-sizing: border-box; margin: 0; padding: 0; }
  html, body { width: 1200px; height: 900px; overflow: hidden; background: var(--stage); }
  .stage {
    width: 1200px; height: 900px;
    display: flex; align-items: center; justify-content: center; gap: 40px;
  }
  .card {
    width: 540px; height: 310px;
    background: var(--card);
    box-shadow: 0 18px 40px rgba(0,0,0,.55);
    position: relative;
  }

  /* Front */
  .card-front { display: flex; align-items: center; }
  .brand-spot {
    width: 260px; height: 100%;
    padding: 0 36px 0 40px;
    display: flex; align-items: center; justify-content: center; gap: 14px;
  }
  .brand-dot { width: 18px; height: 18px; border-radius: 50%; background: var(--gold); flex: none; }
  .brand-name {
    font-family: "Cinzel", serif; font-weight: 600; font-size: 24px; line-height: 1.15;
    color: var(--gold); letter-spacing: .5px;
  }
  .brand-name span { display: block; }
  .divider { width: 1px; height: 170px; background: var(--silver-dim); flex: none; }
  .details { padding-left: 24px; font-family: "Tinos", serif; color: var(--silver); }
  .person-name {
    font-family: "Cinzel", serif; font-weight: 600; font-size: 19px;
    color: var(--silver); letter-spacing: 1px;
  }
  .person-title {
    font-family: "Cinzel", serif; font-weight: 600; font-size: 10px;
    color: var(--gold); letter-spacing: .8px; margin-bottom: 12px;
  }
  .address { font-size: 12.5px; line-height: 1.35; margin-bottom: 12px; }
  .contact-list { list-style: none; font-size: 12.5px; line-height: 1.65; }
  .contact-list li { display: flex; align-items: center; gap: 9px; }
  .contact-list svg { width: 12px; height: 12px; flex: none; }

  /* Back */
  .card-back {
    display: flex; flex-direction: column; align-items: center; justify-content: center;
  }
  .back-mark { display: flex; align-items: center; gap: 14px; margin-bottom: 10px; }
  .back-dot { width: 26px; height: 26px; border-radius: 50%; background: var(--gold); }
  .back-name {
    font-family: "Cinzel", serif; font-weight: 600; font-size: 34px;
    color: var(--gold); letter-spacing: 1px;
  }
  .back-services {
    font-family: "Montserrat", sans-serif; font-weight: 300; font-size: 15px;
    color: var(--silver); letter-spacing: 6px; margin-bottom: 8px;
  }
  .back-lines {
    font-family: "Montserrat", sans-serif; font-weight: 500; font-size: 11px;
    color: var(--white); letter-spacing: 1.5px;
  }
</style>
</head>
<body>
<main class="stage">
  <section class="card card-front">
    <div class="brand-spot">
      <span class="brand-dot"></span>
      <p class="brand-name"><span>Harborline</span><span>Crest</span></p>
    </div>
    <div class="divider"></div>
    <div class="details">
      <p class="person-name">MARCUS HALE</p>
      <p class="person-title">MANAGING DIRECTOR</p>
      <p class="address">Level 9, 72 Quayside Road<br>Sydney NSW 2000</p>
      <ul class="contact-list">
        <li>
          <svg viewBox="0 0 12 12" aria-hidden="true"><rect x="3" y="0.5" width="6" height="11" rx="1" fill="none" stroke="var(--gold)" stroke-width="1.2"/><circle cx="6" cy="9.5" r=".7" fill="var(--gold)"/></svg>
          0417-282-904
        </li>
        <li>
          <svg viewBox="0 0 12 12" aria-hidden="true"><path d="M2.5 1 L4.5 1 L5.3 3.6 L4 4.6 Q5 7 7.4 8 L8.4 6.7 L11 7.5 L11 9.5 Q10.5 11 9 11 Q1 10 1 2.5 Q1 1 2.5 1Z" fill="var(--gold)"/></svg>
          0756-410-332
        </li>
        <li>
          <svg viewBox="0 0 12 12" aria-hidden="true"><rect x="0.5" y="2" width="11" height="8" fill="var(--gold)"/><path d="M0.8 2.3 L6 6.5 L11.2 2.3" fill="none" stroke="var(--card)" stroke-width="1"/></svg>
          marcushale@harborlinecrest.com
        </li>
        <li>
          <svg viewBox="0 0 12 12" aria-hidden="true"><circle cx="6" cy="6" r="5.3" fill="var(--gold)"/><path d="M0.7 6 H11.3 M6 0.7 V11.3 M6 0.7 Q2.5 6 6 11.3 M6 0.7 Q9.5 6 6 11.3" fill="none" stroke="var(--card)" stroke-width=".7"/></svg>
          harborlinecrest.com
        </li>
      </ul>
    </div>
  </section>

  <section class="card card-back">
    <div class="back-mark">
      <span class="back-dot"></span>
      <span class="back-name">Harborline Crest</span>
    </div>
    <p class="back-services">INSURANCE SERVICES</p>
    <p class="back-lines">AUTO | HOME | BUSINESS | LIFE</p>
  </section>
</main>
</body>
</html>
```